A new website for Electrical Contractor Business

We are looking for a unique and new WordPress website design which would include 5 Pages - Home Page, Meet the Team, Our Services, Our Projects and Contact Us page.

The global theme for the website needs to be professional but simple to navigate as we cater for both business and home owner customers.

Our core business service is targeted around lighting from single room decorative to large office so the theme should incorporate this in some way.

The home page should include;
Our business logo, Contact number, Email address, small Image rotation box - Highlighting pervious projectsText box - With welcome message, chirpnet feed news reel/Customer feed back box.

I would also like to see a 2 boxes for the separate customer types we services. Business and Home Owner. each box will have a small image with a small text description with a link to the area of the services page relevant to that customer type.

Meet the team page -This will be introducing potential customers to the team so I would like it to include for each team member. Something like a small image and text area which will introduce an outline of the team members skills and abilities.

Our Services page This page will be outlining the different services on offer to the both customer types business and homeowner. Each service should have an image with text description of the service would good here.

Our projects page-Will include images of pervious projects and work we have completed along with a text area for the project description/ outliner.

Contact Us page - Should include a contact form which should include an option for the customer to quest us to call them back, also a selection box for them to inform us our how they found our details would be good.

Colour - The theme colours can be taken from the logo or feel free to impress with your own imagination.

Remember we are looking for a website that will interest our customers enough to except our services or be drawn further into the website.. So call to action links to other areas of the site/ contact page are welcome

Target Market(s)

Business - Office, warehousing and Large Store - lighting and Power
Home owner lighting and power

Coding

Coded - Design and coding required

Number of Pages Required

5+ page

Font styles to use
Serif
Sans Serif

Colors

Designer to choose colors to be used in the design.

Requirements
Must have
• Logo integrated into the website design - i.e. website colours which allow the logo to blend into the design.
Nice to have
• Custom but professional theme catering to business customers, but also show that we do provide services to home owners too.
Should not have
• Sorry am not interested in one oversized block image on rotation covering half the home page.. Images will be needed but not a single block over sized frame with not text, shape. Please use your imagination when considering this design

```html
<!DOCTYPE html>
<html lang="en">
<head>
<meta charset="utf-8">
<title>Contact – Voltline Electrical</title>
<link href="https://fonts.googleapis.com/css2?family=Montserrat:wght@600;700;800&family=Nunito+Sans:wght@400;600;700&display=swap" rel="stylesheet">
<style>
:root{
  --navy:#1e2f5e;
  --orange:#f26a2b;
  --text:#3b3f4a;
  --field:#f0f0f0;
  --field-line:#cfcfcf;
  --white:#ffffff;
}
*{box-sizing:border-box;margin:0;padding:0}
html,body{width:795px;height:1200px;overflow:hidden;background:var(--white)}
body{position:relative;font-family:"Nunito Sans",sans-serif;color:var(--text)}
.abs{position:absolute}
/* header */
.top-line{left:0;top:0;width:795px;height:1px;background:var(--navy)}
.brand{left:50px;top:18px;display:flex;align-items:center;gap:7px}
.brand-mark{width:30px;height:30px;border-radius:50%;border:2px solid var(--orange)}
.brand-name{font-weight:700;font-size:11.5px;letter-spacing:1px;color:var(--navy)}
.contact-chip{top:15px;display:flex;align-items:center;gap:12px}
.chip-icon{width:31px;height:31px;border-radius:50%;border:1px solid var(--orange);display:flex;align-items:center;justify-content:center}
.chip-label{font-size:9px;letter-spacing:.5px;color:var(--text);line-height:12px}
.chip-value{font-size:12px;color:var(--text);line-height:17px}
.nav{left:0;top:62px;width:795px;height:35px;background:var(--orange)}
.nav a{position:absolute;top:0;height:35px;line-height:35px;font-size:9.3px;color:var(--white);text-decoration:none;letter-spacing:.3px}
.nav a.active{background:var(--navy);width:78px;left:399px;text-align:center}
.nav a.cta{background:var(--navy);width:110px;left:635px;text-align:center;font-family:"Montserrat",sans-serif;font-weight:700;font-size:10px}
/* intro */
.page-title{left:0;width:795px;top:140px;text-align:center;font-family:"Montserrat",sans-serif;font-weight:800;font-size:24px;color:var(--navy);letter-spacing:.5px}
.page-intro{left:135px;width:525px;top:175px;text-align:center;font-size:8.8px;line-height:16.5px}
.section-title{top:242px;font-family:"Montserrat",sans-serif;font-weight:700;font-size:15.5px;color:var(--navy)}
.info-row{display:flex;gap:14px;font-size:8.8px;line-height:16.5px}
.info-row svg{flex:none;margin-top:2px}
.social{top:373px;width:32px;height:32px;border-radius:50%;border:1.5px solid var(--navy);display:flex;align-items:center;justify-content:center;font-size:6px;font-weight:700;color:var(--navy);letter-spacing:0}
.social.alt{border-color:var(--orange);color:var(--orange)}
/* form */
.field{background:var(--field);border:1px solid var(--field-line);font-size:9px;color:#555;padding:0 11px;display:flex;align-items:center}
.field.area{align-items:flex-start;padding-top:11px}
.field svg{margin-left:auto}
.send{left:401px;top:518px;width:180px;height:35px;background:var(--orange);color:var(--white);font-family:"Montserrat",sans-serif;font-weight:700;font-size:12.5px;letter-spacing:.5px;display:flex;align-items:center;justify-content:center}
.map{left:50px;top:592px;width:696px;height:270px;border:1px solid var(--orange);background:linear-gradient(135deg,#e9eee0 0%,#dfe9cf 35%,#ece9e1 60%,#e4ecd8 100%)}
/* footer */
.footer{left:0;top:930px;width:795px;height:229px;background:var(--navy)}
.footer-brand{left:50px;top:966px;display:flex;align-items:center;gap:9px}
.footer-brand .brand-mark{width:44px;height:44px;border-color:var(--white)}
.footer-brand .brand-name{color:var(--white);font-size:13px}
.footer-text{font-size:8.8px;line-height:16.5px;color:var(--white)}
.footer-title{top:972px;font-family:"Montserrat",sans-serif;font-weight:700;font-size:12.5px;color:var(--orange);letter-spacing:.3px}
.tweet-dot{width:15px;height:15px;border-radius:50%;background:var(--white)}
.tweet-time{font-size:8.8px;color:var(--orange)}
.copyright{left:0;top:1159px;width:795px;height:41px;background:var(--orange);color:var(--white);font-size:9px;text-align:center;line-height:41px}
</style>
</head>
<body>
<svg width="0" height="0" style="position:absolute">
  <defs>
    <symbol id="pin" viewBox="0 0 12 16"><path d="M6 0a6 6 0 0 0-6 6c0 4.5 6 10 6 10s6-5.5 6-10a6 6 0 0 0-6-6zm0 8.5A2.5 2.5 0 1 1 6 3.5a2.5 2.5 0 0 1 0 5z" fill="currentColor"/></symbol>
    <symbol id="phone" viewBox="0 0 16 16"><path d="M3.6 1l2.3 3.2-1.4 1.7c.9 2 2.6 3.7 4.6 4.6l1.7-1.4L14 11.4 12.8 14C6.5 14.3 1.7 9.5 2 3.2z" fill="currentColor"/></symbol>
    <symbol id="mail" viewBox="0 0 16 12"><path d="M0 0h16v2L8 7 0 2zM0 4l8 5 8-5v8H0z" fill="currentColor"/></symbol>
  </defs>
</svg>

<header>
  <div class="abs top-line"></div>
  <div class="abs brand"><span class="brand-mark"></span><span class="brand-name">VOLTLINE ELECTRICAL</span></div>
  <div class="abs contact-chip" style="left:406px">
    <span class="chip-icon"><svg width="12" height="9" style="color:var(--navy)"><use href="#mail"/></svg></span>
    <div><div class="chip-label">EMAIL US ON</div><div class="chip-value">info@voltline-electric.com</div></div>
  </div>
  <div class="abs contact-chip" style="left:609px">
    <span class="chip-icon"><svg width="12" height="12" style="color:var(--navy)"><use href="#phone"/></svg></span>
    <div><div class="chip-label">CALL US ON</div><div class="chip-value">555 014 2378</div></div>
  </div>
  <nav class="abs nav">
    <a style="left:64px">HOME</a>
    <a style="left:124px">MEET THE TEAM</a>
    <a style="left:234px">OUR SERVICES</a>
    <a style="left:334px">PROJECTS</a>
    <a class="active">CONTACT</a>
    <a class="cta">GET IN TOUCH</a>
  </nav>
</header>

<main>
  <h1 class="abs page-title">CONTACT</h1>
  <p class="abs page-intro">Lorem Ipsum is simply dummy text of the printing and typesetting industry. Lorem Ipsum has been the industry's standard dummy text ever since the 1500s, when an unknown printer took a galley.</p>

  <h2 class="abs section-title" style="left:53px">Contact Info</h2>
  <div class="abs info-row" style="left:51px;top:272px;width:200px">
    <svg width="12" height="16" style="color:var(--orange)"><use href="#pin"/></svg>
    <span>Lorem Ipsum is simply dummy text of the printing and typesetting industry.</span>
  </div>
  <div class="abs info-row" style="left:51px;top:314px">
    <svg width="14" height="14" style="color:var(--orange)"><use href="#phone"/></svg><span>555 014 2378</span>
  </div>
  <div class="abs info-row" style="left:51px;top:339px">
    <svg width="13" height="10" style="color:var(--orange);margin-top:4px"><use href="#mail"/></svg><span>info@voltline-electric.com</span>
  </div>
  <span class="abs social" style="left:50px">Pallyhub</span>
  <span class="abs social alt" style="left:92px">chirpnet</span>
  <span class="abs social" style="left:133px">Workly</span>

  <h2 class="abs section-title" style="left:399px">Get In Touch With Us</h2>
  <div class="abs field" style="left:401px;top:277px;width:159px;height:35px">Name</div>
  <div class="abs field" style="left:574px;top:277px;width:159px;height:35px">Contact No.</div>
  <div class="abs field" style="left:401px;top:325px;width:332px;height:35px">Email</div>
  <div class="abs field" style="left:401px;top:373px;width:332px;height:35px">How did you find us
    <svg width="13" height="8" viewBox="0 0 13 8"><path d="M1 1l5.5 5.5L12 1" fill="none" stroke="#666" stroke-width="1.6"/></svg>
  </div>
  <div class="abs field area" style="left:401px;top:422px;width:332px;height:83px">Message</div>
  <div class="abs send">SEND MESSAGE</div>

  <div class="abs map" role="img" aria-label="Map of the southwestern and central United States showing the service area"></div>
</main>

<footer>
  <div class="abs footer"></div>
  <div class="abs footer-brand"><span class="brand-mark"></span><span class="brand-name">VOLTLINE ELECTRICAL</span></div>
  <p class="abs footer-text" style="left:53px;top:1027px;width:190px">Lorem Ipsum is simply dummy text of the printing and typesetting industry. Lorem Ipsum has been the industry's standard.</p>

  <h3 class="abs footer-title" style="left:292px">RECENT CHIRPS</h3>
  <span class="abs tweet-dot" style="left:294px;top:1002px"></span>
  <p class="abs footer-text" style="left:324px;top:997px;width:170px">Lorem Ipsum is simply dummy text of the printing and typesetting industry.</p>
  <span class="abs tweet-time" style="left:324px;top:1034px">4 days ago</span>
  <span class="abs tweet-dot" style="left:294px;top:1068px"></span>
  <p class="abs footer-text" style="left:324px;top:1063px;width:170px">Lorem Ipsum is simply dummy text of the printing and typesetting industry.</p>
  <span class="abs tweet-time" style="left:324px;top:1100px">4 days ago</span>

  <h3 class="abs footer-title" style="left:532px">CONTACT INFO</h3>
  <div class="abs info-row footer-text" style="left:530px;top:997px;width:200px">
    <svg width="12" height="16" style="color:var(--orange)"><use href="#pin"/></svg>
    <span>Lorem Ipsum is simply dummy text of the printing and typesetting industry.</span>
  </div>
  <div class="abs info-row footer-text" style="left:530px;top:1039px">
    <svg width="14" height="14" style="color:var(--orange)"><use href="#phone"/></svg><span>555 014 2378</span>
  </div>
  <div class="abs info-row footer-text" style="left:530px;top:1064px">
    <svg width="13" height="10" style="color:var(--orange);margin-top:4px"><use href="#mail"/></svg><span>info@voltline-electric.com</span>
  </div>

  <div class="abs copyright">©VOLTLINE ELECTRICAL– 2019. All Rights Reserved.</div>
</footer>
</body>
</html>
```